Presentation Folder, for Cancer Awareness, VERY COLORFULL AND MODERN

This will be a standard size folder that will hold standard 8 1/2 x 11 papers with a business card slot on the flap, this is a very easy project with very little text and the design for the back page is already done so all you really have to do is make a very nice colorful front cover, you will see my attachments are labeled and I gave you alot of instructions, this should be a very fast easy project
Updates

Reason: there has not been enough quality designs, sorry

Target Market(s)

Our Target Market is Dr's that Deal with Cancer patients

Industry/Entity Type

Healthcare

Font styles to use
Serif

Colors

Designer to choose colors to be used in the design.

Requirements
Must have
• Project must be tasteful and look professional with the ribbons as the main focal point in the center of folder the folder should be a nice gray color to accent the color of the ribbons , the back page needs no design it is the" Velmora Test" in the attachments I sent
Nice to have
• I would like the ribbons displayed in a row, I included a logo sample layout
• a picture on the front of the folder under the words Hereditary Cancer Screening - Then under that put the words - The Power of Knowledge - then add the picture I labeled Great Picture in the attachments

```html
<!DOCTYPE html>
<html lang="en">
<head>
<meta charset="utf-8">
<title>Hereditary Cancer Screening – Folder Cover</title>
<link rel="stylesheet" href="https://fonts.googleapis.com/css2?family=Arimo:wght@400;700&display=swap">
<style>
  :root {
    --backdrop: #c9c9c9;
    --cover-dark: #1f1f21;
    --cover-mid: #2e2e31;
    --title-pink: #e0559a;
    --text-light: #f1f1f1;
    --text-muted: #b9b9bd;
    --brand-red: #c9302c;
    --ghost: rgba(255,255,255,0.10);
    --tone-warm: #c98f86;
    --tone-rose: #d97fb4;
    --tone-violet: #9a7cc9;
    --tone-blue: #8fb7de;
    --tone-green: #7fae78;
  }
  * { box-sizing: border-box; margin: 0; padding: 0; }
  html, body {
    width: 1200px; height: 789px; overflow: hidden;
    background: var(--backdrop);
    font-family: "Arimo", Arial, sans-serif;
  }
  .folder-cover {
    position: absolute; left: 329px; top: 44px;
    width: 541px; height: 700px;
    background: radial-gradient(ellipse at 50% 30%, var(--cover-mid), var(--cover-dark) 75%);
    box-shadow: 0 8px 24px rgba(0,0,0,0.25);
    text-align: center; color: var(--text-light);
  }
  .brand {
    position: absolute; top: 64px; left: 0; right: 0;
    display: flex; flex-direction: column; align-items: center; gap: 10px;
  }
  .brand-dot {
    width: 34px; height: 34px; border-radius: 50%;
    background: var(--brand-red);
  }
  .brand-name {
    font-size: 14px; letter-spacing: 5px; text-transform: uppercase;
    color: var(--text-light); font-weight: 400;
  }
  .headline {
    position: absolute; top: 158px; left: 0; right: 0;
    font-size: 28px; font-weight: 400; color: var(--title-pink);
  }
  .tagline {
    position: absolute; top: 196px; left: 0; right: 0;
    font-size: 19px; font-weight: 400; color: var(--text-light);
  }
  .feature-art {
    position: absolute; top: 248px; left: 105px;
    width: 330px; height: 330px; border-radius: 50%;
    background:
      radial-gradient(circle at 50% 50%, var(--tone-warm) 0, rgba(201,143,134,0) 45%),
      linear-gradient(135deg, var(--tone-green), var(--tone-violet) 40%, var(--tone-rose) 70%, var(--tone-blue));
    opacity: 0.85;
  }
  .ghost-word {
    position: absolute; top: 572px; left: 0; right: 0;
    font-size: 44px; letter-spacing: 16px; color: var(--ghost);
    font-weight: 400;
  }
  .cancer-types {
    position: absolute; top: 606px; left: 0; right: 0;
    font-size: 11px; color: var(--text-muted); word-spacing: 1px;
  }
</style>
</head>
<body>
  <main class="folder-cover">
    <div class="brand">
      <span class="brand-dot"></span>
      <span class="brand-name">Corvane Labs</span>
    </div>
    <h1 class="headline">Hereditary Cancer Screening</h1>
    <p class="tagline">The Power of Knowledge</p>

    <div class="feature-art" role="img" aria-label="Ring of colourful cancer awareness ribbons framing a photo of a smiling older man and young woman"></div>

    <div class="ghost-word" aria-hidden="true">CANCER</div>
    <p class="cancer-types">Breast | Ovarian | Endometrial | Gastric | Colorectal | Pancreatic | Melanoma | Prostate | Lung | Colon</p>
  </main>
</body>
</html>
```